Adult Literacy Program - flyer to attract volunteers and students

We want a flyer that is engaging, colorful, modern and will appeal to our primary audience of adults aged 40-60. We are trying to attract both prospective volunteers (typically age 50+, mostly women) and students (typically aged 40+).
The flyer should feature diverse people working together in pairs of two, reading or talking, with a workbook or some reading material in front of them.

Our organization trains tutors to work one-on-one with adults who are learning how to read. Most of our adult students are non-native speakers of English. Many are of Haitian or Hispanic origin, so we would like some people who represent that demographic.

The Flyer should represent reading, learning, literacy, knowledge, growth,
and opportunities.
Our students are learning to read so they can advance their job opportunities.

Target Market(s)

Adults aged 40-60, primarily women, retired, volunteers

Industry/Entity Type

Education

Font styles to use
Serif
Sans Serif

Colors

Designer to choose colors to be used in the design.

Requirements
Must have
• - UPDATE: Should be designed as a TRI-FOLD brochure on 8.5 x 11 inch paper that will be folded into thirds.
• - Images of diverse people, women and men, who look Hispanic, Haitian and other nationalities as well as Caucasian.
• - Our logo on the front cover
Nice to have
• The sample flyer is very boring and dry! We are open to different ways of presenting the text.

```html
<!DOCTYPE html>
<html lang="en">
<head>
<meta charset="utf-8">
<title>Adult Literacy Project – Tri-fold Brochure</title>
<link rel="stylesheet" href="https://fonts.googleapis.com/css2?family=Open+Sans:wght@300;400;600;700;800&display=swap">
<style>
  :root{
    --backdrop:#333333;
    --navy:#0b0d7e;
    --ink-navy:#13215f;
    --blue:#00aedb;
    --aqua:#d4fdfe;
    --paper:#ffffff;
    --mist:#f2f2f2;
    --ink:#111111;
  }
  html,body{margin:0;padding:0;width:1200px;height:1200px;overflow:hidden;background:var(--backdrop);}
  body{font-family:"Open Sans",sans-serif;color:var(--ink);}
  .stage{position:absolute;left:0;top:0;width:1500px;height:1500px;transform:scale(.8);transform-origin:0 0;}
  .sheet{position:absolute;left:328px;width:814px;overflow:hidden;}
  .sheet--outside{top:85px;height:628px;background:var(--aqua);}
  .sheet--inside{top:788px;height:625px;background:var(--mist);}
  .sheet svg.shapes{position:absolute;left:0;top:0;}
  .abs{position:absolute;}
  .center{text-align:center;}
  .photo{position:absolute;border-radius:50%;box-sizing:border-box;}

  /* outside */
  .cover-corner{left:0;top:0;width:120px;height:120px;background:var(--blue);}
  .cover-box{left:0;top:0;width:265px;height:400px;background:var(--paper);border-right:6px solid var(--blue);border-bottom:7px solid var(--blue);border-top-left-radius:72px 90px;}
  .headline{left:0;width:265px;top:40px;font-weight:800;font-size:30px;line-height:37px;color:var(--ink-navy);letter-spacing:.5px;}
  .mark{display:flex;align-items:center;justify-content:center;gap:10px;font-weight:700;color:var(--ink-navy);}
  .mark .dot{width:22px;height:22px;border-radius:50%;background:var(--blue);}
  .promise{left:0;width:265px;top:296px;font-weight:600;font-size:19px;line-height:31px;}
  .perks{left:22px;top:430px;margin:0;padding:0;list-style:none;font-weight:600;font-size:14.5px;line-height:31px;}
  .perks li{padding-left:10px;text-indent:-8px;}
  .perks li::before{content:"• ";font-size:10px;}
  .contact{left:271px;width:276px;font-weight:700;font-size:18.5px;line-height:31px;}
  .contact .row{display:flex;align-items:center;justify-content:center;gap:10px;}
  .contact svg{flex:none;}
  .contact .small{font-size:15px;}
  .url-bar{left:271px;top:592px;width:543px;height:36px;background:var(--navy);color:#fff;font-weight:700;font-size:17px;display:flex;}
  .url-bar span{flex:1;text-align:center;line-height:36px;}

  /* inside */
  .panel-title{font-weight:700;font-size:23px;letter-spacing:.3px;}
  .url{font-weight:700;font-size:17px;color:#222;width:271px;text-align:center;top:598px;}
  .tutor-list,.student-list{margin:0;padding:0;list-style:none;font-weight:400;font-size:12.5px;line-height:24.5px;}
  .tutor-list{left:280px;top:355px;color:#fff;width:260px;}
  .student-list{left:558px;top:330px;color:#222;width:255px;}
  .tutor-list li::before,.student-list li::before{content:"• ";font-size:9px;}
  .tutor-list li.cont::before{content:none;}
  .tutor-list .cont{padding-left:9px;}
  .student-list .sub{padding-left:38px;}
  .callout{font-weight:700;font-size:14px;line-height:25px;letter-spacing:.2px;}
  .badge{left:61px;top:458px;width:150px;height:108px;background:var(--paper);display:flex;align-items:center;justify-content:center;}
  .badge .mark{font-size:15px;gap:7px;}
  .badge .mark .dot{width:16px;height:16px;}
</style>
</head>
<body>
<main class="stage">

  <!-- Outside of brochure -->
  <section class="sheet sheet--outside">
    <svg class="shapes" width="814" height="628" viewBox="0 0 814 628">
      <polygon points="271,0 814,0 814,300 446,10 271,130" fill="var(--paper)"/>
      <polyline points="271,130 446,8 814,296" fill="none" stroke="var(--blue)" stroke-width="22"/>
      <polyline points="271,178 446,46 814,346" fill="none" stroke="var(--navy)" stroke-width="22"/>
    </svg>

    <div class="abs cover-corner"></div>
    <div class="abs cover-box"></div>
    <h1 class="abs headline center" style="margin:0">CONNECT<br>INSPIRE<br>ENRICE</h1>
    <div class="abs mark" style="left:0;width:265px;top:230px;font-size:17px"><span class="dot"></span>Riverbend Reads</div>
    <p class="abs promise center" style="margin:0">A highly rewarding<br>experience awaits<br>you!</p>

    <ul class="abs perks">
      <li>Volunteer a few thours each<br>week and make a difference.</li>
      <li>Teach an adult to read,<br>write or speak English.</li>
      <li>Materials and training are<br>offered free-of-charge.</li>
    </ul>

    <div class="abs mark" style="left:271px;width:276px;top:172px;font-size:17px"><span class="dot"></span>Riverbend Reads</div>

    <div class="abs contact center" style="top:213px">
      Don’t waste a moment!<br>Contact us today<br>to learn more.
    </div>
    <div class="abs contact center" style="top:337px">
      Volunteer Desk
      <div class="row">
        <svg width="22" height="22" viewBox="0 0 24 24" fill="none" stroke="#111" stroke-width="1.8"><path d="M5 3h4l2 5-2.5 1.5a11 11 0 0 0 6 6L16 13l5 2v4a2 2 0 0 1-2 2A17 17 0 0 1 3 5a2 2 0 0 1 2-2z"/></svg>
        555-014-7510
      </div>
    </div>
    <div class="abs contact center" style="top:429px;left:279px">
      <div class="row">
        <svg width="18" height="22" viewBox="0 0 24 28" fill="none" stroke="#111" stroke-width="2"><path d="M12 26s9-9 9-15a9 9 0 0 0-18 0c0 6 9 15 9 15z"/><circle cx="12" cy="11" r="3"/></svg>
        Oakridge, Millbrook &amp;
      </div>
      Cedar Bay
      <div class="row">
        <svg width="22" height="22" viewBox="0 0 24 24" fill="none" stroke="#111" stroke-width="1.8"><path d="M5 3h4l2 5-2.5 1.5a11 11 0 0 0 6 6L16 13l5 2v4a2 2 0 0 1-2 2A17 17 0 0 1 3 5a2 2 0 0 1 2-2z"/></svg>
        555-013-3453
      </div>
      <div class="row small">
        <svg width="22" height="16" viewBox="0 0 24 18" fill="none" stroke="#111" stroke-width="1.8"><rect x="1" y="1" width="22" height="16"/><path d="M1 1l11 9 11-9M1 17l8-7M23 17l-8-7"/></svg>
        literacy@riverbendlibrary.org
      </div>
    </div>

    <div class="photo" role="img" aria-label="Photo: a young woman tutor reading a book with an elderly man" style="left:547px;top:13px;width:264px;height:264px;border:9px solid var(--blue);background:radial-gradient(circle at 40% 45%,#efe6dc,#c9b9a8 60%,#8e7f70);"></div>

    <div class="abs mark" style="left:547px;width:267px;top:520px;font-size:22px"><span class="dot"></span>Riverbend Reads</div>

    <div class="abs url-bar"><span>www.riverbendlibrary.org</span><span>www.riverbendlibrary.org</span></div>
  </section>

  <!-- Inside of brochure -->
  <section class="sheet sheet--inside">
    <svg class="shapes" width="814" height="625" viewBox="0 0 814 625">
      <polygon points="0,0 271,0 271,50 0,330" fill="var(--navy)"/>
      <line x1="0" y1="338" x2="271" y2="58" stroke="var(--aqua)" stroke-width="10"/>
      <rect x="97" y="0" width="77" height="110" fill="var(--blue)"/>
      <rect x="271" y="0" width="271" height="594" fill="var(--blue)"/>
      <rect x="361" y="0" width="93" height="120" fill="var(--paper)"/>
      <rect x="271" y="594" width="271" height="31" fill="var(--paper)"/>
      <polygon points="570,0 814,0 814,196" fill="var(--navy)"/>
      <line x1="546" y1="0" x2="814" y2="215" stroke="var(--navy)" stroke-width="9"/>
      <line x1="555" y1="0" x2="814" y2="205" stroke="var(--aqua)" stroke-width="7"/>
      <rect x="640" y="0" width="77" height="110" fill="var(--blue)"/>
    </svg>

    <div class="photo" role="img" aria-label="Photo: a smiling woman volunteer seated beside an older man" style="left:34px;top:66px;width:202px;height:202px;border:11px solid var(--blue);background:radial-gradient(circle at 50% 45%,#e6ddd1,#a8a596 60%,#5f6a55);"></div>
    <div class="abs panel-title center" style="left:0;width:271px;top:272px">VOLUNTEER</div>
    <div class="abs center" style="left:0;width:261px;top:322px;font-weight:600;font-size:22px">Enrich a Life!</div>
    <div class="abs center" style="left:0;width:263px;top:368px;font-weight:700;font-size:19.5px;line-height:25px">Help an adult to<br>read, write or<br>speak English</div>
    <div class="abs badge">
      <div class="mark"><span class="dot"></span>Riverbend Library</div>
    </div>
    <div class="abs url" style="left:0">www.riverbendlibrary.org</div>

    <div class="photo" role="img" aria-label="Photo: a young man and a woman tutor studying together at a table with books" style="left:285px;top:60px;width:244px;height:244px;border:11px solid var(--paper);background:radial-gradient(circle at 55% 45%,#f1ece6,#b89a86 55%,#6b4b3c);"></div>
    <div class="abs panel-title center" style="left:271px;width:271px;top:311px">TUTORE</div>
    <ul class="abs tutor-list">
      <li>No special skills or degrees needed —</li>
      <li class="cont">just &nbsp;a degree of caring!</li>
      <li>Training offered throug hout &nbsp;the year</li>
      <li>Tutors meet students weekly at a library</li>
      <li>Instructional materials provided</li>
      <li>Ongoing support available</li>
    </ul>
    <div class="abs callout center" style="left:271px;width:271px;top:509px">TEACH AN ADULT TO READ AND<br>YOU’LL CHANGE A LIFE FOREVER.</div>
    <div class="abs url" style="left:271px">www.riverbendlibrary.org</div>

    <div class="photo" role="img" aria-label="Photo: an older man and woman student reading together at a table" style="left:578px;top:66px;width:202px;height:202px;border:11px solid var(--blue);background:radial-gradient(circle at 50% 45%,#ece7e2,#bba6b7 55%,#7b8a5c);"></div>
    <div class="abs panel-title center" style="left:543px;width:271px;top:272px">STUDENT</div>
    <ul class="abs student-list" style="top:328px">
      <li>Students are adults in need of</li>
      <li class="sub">basic literacy skills</li>
      <li class="sub">pre GED skills</li>
      <li class="sub">conversational English</li>
      <li>Tutoring is free of charge</li>
      <li>Tutoring is one-on-one</li>
      <li>Flexible scheduling during library hours</li>
      <li>Lessons focus on student goals</li>
    </ul>
    <div class="abs callout center" style="left:543px;width:271px;top:528px">IF YOU CAN READ, YOU CAN TUTOR!</div>
    <div class="abs url" style="left:543px">www.riverbendlibrary.org</div>
  </section>

</main>
</body>
</html>
```